Dental Practice Website design

Design a new website for Bramblewick Dental Practice.
Design should be warm, neutral in colour, with some small amount of bright colour if needed but kept to a minimum. Website should look professional, high end. Home page should be easy to navigate and simple for patients to be able to book online.
Logo in files along with some examples of websites that we like. Please ask if any further info needed.
Menu should have:
About
New Patients
Treatments
Fees
Contact Us
Updates

Industry/Entity Type

Dentistry

Number of Pages Required

4 page

Font styles to use
Sans Serif

Colors

Designer to choose colors to be used in the design.

Requirements
Must have
• google reviews badge, book online button,
Nice to have
• neutral, relaxing colours
Should not have
• harsh, bright colours!

```html
<!DOCTYPE html>
<html lang="en">
<head>
<meta charset="utf-8">
<title>Bramblewick Dental Practice</title>
<link href="https://fonts.googleapis.com/css2?family=Roboto:wght@300;400;500;700;900&display=swap" rel="stylesheet">
<style>
:root{
  --ink:#262b2a;
  --ink-soft:#3a3f3d;
  --accent:#6e9f9c;
  --accent-2:#86ab9c;
  --accent-dark:#557f7c;
  --soft-bg:#f4f2ec;
  --text:#4c4f4d;
  --heading:#4a4d4b;
  --white:#ffffff;
  --field:#cfd3c8;
  --star:#c9a86a;
}
*{margin:0;padding:0;box-sizing:border-box}
html,body{width:1200px;height:4222px;overflow:hidden}
body{font-family:'Roboto',sans-serif;color:var(--text);background:var(--white);position:relative}
.abs{position:absolute}
.btn{position:absolute;display:flex;align-items:center;justify-content:center;border-radius:40px;background:var(--accent);color:var(--white);font-weight:500;text-decoration:none;white-space:nowrap}
.photo{position:absolute;border-radius:34px}

/* hero */
.hero{position:absolute;left:0;top:0;width:1200px;height:756px;background:var(--ink)}
.brand{position:absolute;left:160px;top:36px;color:#d8d6cf;font-weight:300;letter-spacing:1px}
.brand .b1{font-size:30px;line-height:34px}
.brand .b2{font-size:15px;letter-spacing:1.5px}
.call{left:674px;top:34px;color:#e6e3dc;font-size:14px;letter-spacing:.6px}
.top-book{left:869px;top:23px;width:172px;height:40px;font-size:11px;letter-spacing:.4px}
.nav{position:absolute;right:159px;top:86px;display:flex;gap:16px;font-size:13px;color:var(--white)}
.hero h1{position:absolute;left:160px;top:186px;width:320px;color:var(--white);font-size:25px;line-height:38px;font-weight:900;text-transform:uppercase}
.hero p.lead{position:absolute;left:160px;top:312px;width:310px;color:#e2dfd8;font-size:12.5px;line-height:24px}
.hero-book{left:159px;top:387px;width:157px;height:41px;font-size:13px;font-weight:400}
.hero-rule{position:absolute;left:160px;top:475px;width:296px;height:1px;background:#474c4a}
.feat{position:absolute;top:518px;display:flex;align-items:center;gap:14px;color:var(--white);font-size:12.5px;line-height:18px;font-weight:500}
.feat .ic{width:52px;height:48px;border-radius:8px;background:#535957;display:flex;align-items:center;justify-content:center}
.reviews{position:absolute;left:160px;top:608px;width:296px;height:52px;border:1px solid #535957;border-radius:8px;display:flex;align-items:center;gap:14px;padding:0 14px}
.reviews .mark{width:28px;height:28px;border-radius:50%;background:#e8e4da}
.reviews .stars{display:flex;gap:4px}

/* info band */
.band{position:absolute;left:0;top:756px;width:1200px;height:132px;display:flex}
.band .cell{flex:1;display:flex;align-items:center;padding-left:97px;gap:18px;color:var(--white);background:linear-gradient(90deg,var(--accent),var(--accent-2))}
.band .cell:nth-child(2){padding-left:64px}
.band .cell:nth-child(3){padding-left:60px}
.band .ic{width:52px;height:46px;background:var(--white);border-radius:8px;display:flex;align-items:center;justify-content:center;flex:none}
.band h4{font-size:15.5px;font-weight:500}
.band small{font-size:12px;opacity:.95;white-space:nowrap}

/* welcome */
.welcome-img{left:160px;top:946px;width:428px;height:477px;background:linear-gradient(135deg,#c9a98c,#7a4d34 55%,#e6e2dc)}
.years{position:absolute;left:428px;top:1336px;width:183px;height:116px;background:var(--ink-soft);border-radius:10px;color:var(--white);text-align:center}
.years b{display:block;font-size:58px;font-weight:500;color:var(--accent-2);line-height:60px;margin-top:12px}
.years b sup{font-size:30px}
.years span{font-size:14px}
.eyebrow{color:var(--accent);font-size:25px;font-weight:500;text-transform:uppercase}
.welcome .eyebrow{position:absolute;left:638px;top:948px}
.welcome h2{position:absolute;left:638px;top:980px;font-size:24.5px;font-weight:500;color:var(--heading);text-transform:uppercase;white-space:nowrap}
.welcome .copy{position:absolute;left:641px;top:1026px;width:400px;font-size:11.3px;line-height:18.2px;text-align:justify;color:var(--text)}
.welcome .copy p{margin-bottom:10px}
.book-online{left:641px;top:1373px;width:162px;height:50px;font-size:14px}

/* services */
.services{position:absolute;left:0;top:1503px;width:1200px;height:611px;background:var(--soft-bg)}
.services .eyebrow{position:absolute;left:161px;top:58px;font-size:18px}
.services h2{position:absolute;left:160px;top:84px;width:520px;font-size:28px;line-height:34px;font-weight:500;color:var(--heading)}
.all-services{left:872px;top:84px;width:169px;height:50px;font-size:16px}
.card{position:absolute;top:195px;height:354px;background:var(--white);border-radius:14px;padding:30px 27px}
.card .head{display:flex;align-items:center;gap:14px;font-size:18px;color:var(--heading);font-weight:400}
.card .ic{width:46px;height:44px;border-radius:8px;background:var(--accent-2);display:flex;align-items:center;justify-content:center}
.card p{margin-top:20px;font-size:11px;line-height:17px;color:#5a5d5b}
.card .pic{position:absolute;left:27px;right:27px;top:184px;height:144px;border-radius:8px}

/* team */
.team h2{position:absolute;left:0;width:1200px;top:2163px;text-align:center;font-size:35px;font-weight:700;color:var(--heading)}
.team .intro{position:absolute;left:190px;width:820px;top:2224px;text-align:center;font-size:11.5px;line-height:19.5px;color:var(--text)}
.team .intro p{margin-bottom:14px}
.member{position:absolute;top:2388px;width:260px;text-align:center}
.member .face{width:246px;height:246px;border-radius:50%;margin:0 auto}
.member h5{margin-top:22px;font-size:15px;font-weight:500;color:#555856}
.member .role{font-size:10.5px;color:#777;margin-top:2px}
.member .bio{font-size:12px;line-height:16px;color:#6a6d6b;margin:10px auto 0;width:230px}
.social{display:flex;gap:12px;justify-content:center;margin-top:24px}
.social i{width:27px;height:27px;border-radius:50%;border:1px solid #dcdbd6;display:block}

/* cta */
.cta{position:absolute;left:0;top:2865px;width:1200px;height:261px;background:linear-gradient(90deg,var(--accent),var(--accent-2));text-align:center;color:var(--white)}
.cta .notch{position:absolute;left:570px;top:0}
.cta h3{position:absolute;left:0;width:1200px;top:56px;font-size:37px;font-weight:700}
.cta p{position:absolute;left:0;width:1200px;top:108px;font-size:19px;font-weight:400;letter-spacing:.3px}
.cta .btn{left:480px;top:159px;width:222px;height:61px;background:var(--white);color:var(--accent-dark);font-size:15px}

/* join */
.join h2{position:absolute;left:161px;top:3170px;font-size:32px;font-weight:500;color:var(--heading)}
.join .copy{position:absolute;left:160px;top:3226px;width:410px;font-size:11px;line-height:18.5px;color:var(--text)}
.join .copy p{margin-bottom:16px}
.join-btn{left:160px;top:3506px;width:160px;height:51px;font-size:16px}
.join-img{position:absolute;left:620px;top:3126px;width:580px;height:490px;background:linear-gradient(135deg,#dcdad4,#b89b85 45%,#9fb9c0 85%)}

/* contact */
.contact{position:absolute;left:0;top:3616px;width:1200px;height:503px;background:var(--soft-bg)}
.contact h2{position:absolute;left:0;width:1200px;top:48px;text-align:center;font-size:38px;font-weight:700;color:var(--heading)}
.field{position:absolute;border:1.5px solid var(--field);background:transparent;padding:18px;font-size:12px;color:#7d807c}
.submit{left:515px;top:408px;width:198px;height:57px;font-size:17px}

/* footer */
.footer{position:absolute;left:0;top:4119px;width:1200px;height:103px;background:var(--ink);color:var(--white)}
.footer .copy{position:absolute;left:162px;top:40px;font-size:12.5px}
.footer .links{position:absolute;left:937px;top:33px;display:flex;gap:8px}
.footer .links i{display:block;width:30px;height:30px;border:1.5px solid var(--white);border-radius:50%}
</style>
</head>
<body>

<header class="hero">
  <div class="brand"><div class="b1">BRAMBLEWICK</div><div class="b2">DENTAL PRACTICE</div></div>
  <div class="abs call">CALL TODAY 240 555 0172</div>
  <a class="btn top-book">BOOK AN APPOINTMENT</a>
  <nav class="nav"><span>HOME</span><span>ABOUT</span><span>NEW PATIENTS</span><span>TREATMENTS</span><span>FEES</span><span>CONTACT US</span><span>UPDATES</span></nav>

  <h1>Exceptional dental care for every stage of your journey</h1>
  <p class="lead">We are committed to providing top-notch dental care in a comfortable and friendly environment.</p>
  <a class="btn hero-book">Book Appointment</a>
  <div class="hero-rule"></div>
  <div class="feat" style="left:160px">
    <div class="ic"><svg width="26" height="26" viewBox="0 0 24 24" fill="none" stroke="#fff" stroke-width="1.3"><circle cx="12" cy="7" r="4"/><path d="M4 22c0-4 4-7 8-7s8 3 8 7"/></svg></div>
    <div>Experience<br>Doctor</div>
  </div>
  <div class="feat" style="left:320px">
    <div class="ic"><svg width="26" height="26" viewBox="0 0 24 24" fill="none" stroke="#fff" stroke-width="1.3"><path d="M12 20s-7-4.5-7-10a4 4 0 0 1 7-2.5A4 4 0 0 1 19 10c0 5.5-7 10-7 10z"/></svg></div>
    <div>Personalized<br>Care</div>
  </div>
  <div class="reviews" role="img" aria-label="Patient reviews badge">
    <div class="mark"></div>
    <div class="stars">
      <svg width="16" height="16" viewBox="0 0 24 24"><path d="M12 2l3 7 7 .6-5.3 4.7 1.6 7.2L12 17.8 5.7 21.5l1.6-7.2L2 9.6 9 9z" fill="var(--star)"/></svg>
      <svg width="16" height="16" viewBox="0 0 24 24"><path d="M12 2l3 7 7 .6-5.3 4.7 1.6 7.2L12 17.8 5.7 21.5l1.6-7.2L2 9.6 9 9z" fill="var(--star)"/></svg>
      <svg width="16" height="16" viewBox="0 0 24 24"><path d="M12 2l3 7 7 .6-5.3 4.7 1.6 7.2L12 17.8 5.7 21.5l1.6-7.2L2 9.6 9 9z" fill="var(--star)"/></svg>
      <svg width="16" height="16" viewBox="0 0 24 24"><path d="M12 2l3 7 7 .6-5.3 4.7 1.6 7.2L12 17.8 5.7 21.5l1.6-7.2L2 9.6 9 9z" fill="var(--star)"/></svg>
      <svg width="16" height="16" viewBox="0 0 24 24"><path d="M12 2l3 7 7 .6-5.3 4.7 1.6 7.2L12 17.8 5.7 21.5l1.6-7.2L2 9.6 9 9z" fill="var(--star)"/></svg>
    </div>
  </div>

  <div class="photo" role="img" aria-label="Smiling woman holding a dental model" style="left:488px;top:149px;width:174px;height:353px;background:linear-gradient(160deg,#d6dcdc,#a57a5f 55%,#9bb7c4)"></div>
  <div class="photo" role="img" aria-label="Young woman smiling in the dental chair" style="left:680px;top:149px;width:174px;height:176px;background:linear-gradient(150deg,#ebeae6,#b88c70 60%,#c08a80)"></div>
  <div class="photo" role="img" aria-label="Smiling young man with beard" style="left:679px;top:341px;width:173px;height:351px;background:linear-gradient(160deg,#e3e4e0,#c09078 55%,#b3cfd3)"></div>
  <div class="photo" role="img" aria-label="Smiling couple" style="left:867px;top:247px;width:174px;height:350px;background:linear-gradient(150deg,#7e5440,#c7937a 55%,#7fa3bd)"></div>
  <div class="photo" role="img" aria-label="Senior patient smiling with dentist" style="left:488px;top:518px;width:174px;height:174px;background:linear-gradient(150deg,#cfcbc5,#9a7664 55%,#6f90ad)"></div>
</header>

<section class="band">
  <div class="cell">
    <div class="ic"><svg width="22" height="22" viewBox="0 0 24 24" fill="none" stroke="var(--accent)" stroke-width="1.6"><path d="M5 3h4l2 5-2.5 1.5a11 11 0 0 0 6 6L16 13l5 2v4a2 2 0 0 1-2 2A17 17 0 0 1 3 5a2 2 0 0 1 2-2z"/></svg></div>
    <div><h4>Need Dental Services ?</h4><small>Call on : (+01) 555 014 392</small></div>
  </div>
  <div class="cell">
    <div class="ic"><svg width="24" height="24" viewBox="0 0 24 24" fill="none" stroke="var(--accent)" stroke-width="1.6"><circle cx="12" cy="12" r="9"/><path d="M12 7v5l3 2"/></svg></div>
    <div><h4>Opening Hours</h4><small>Mon to Sat 9:00AM to 9:00PM</small></div>
  </div>
  <div class="cell">
    <div class="ic"><svg width="24" height="24" viewBox="0 0 24 24" fill="none" stroke="var(--accent)" stroke-width="1.6"><rect x="3" y="5" width="18" height="14" rx="2"/><path d="M3 7l9 6 9-6"/></svg></div>
    <div><h4>Schedule Appointment</h4><small>Mail us : hello@bramblewick.example</small></div>
  </div>
</section>

<section class="welcome">
  <div class="photo welcome-img" role="img" aria-label="Smiling family of three"></div>
  <div class="years"><b>25<sup>+</sup></b><span>Years Of Experience</span></div>
  <div class="eyebrow">Welcome to</div>
  <h2>Bramblewick Dental Practice</h2>
  <div class="copy">
    <p>Welcome to our friendly dental practice nestled in the heart of beautiful Larkfield, UK. Our team of dedicated dentists, hygienists and support staff are here to provide you with exceptional dental care. With a wide array of services, including general and cosmetic dentistry, orthodontics and emergency care, we're confident that we can deliver the highest quality treatment to you and your loved ones.</p>
    <p>At our practice, we believe that a visit to the dentist should be a comfortable and positive experience. We strive to create a warm and welcoming atmosphere where our patients can feel at ease and confident in the care they receive. Our state-of-the-art facilities and equipment mean that you can trust us to deliver the latest techniques and treatments to ensure your oral health is at its best.</p>
    <p>We are passionate about improving dental health and helping you achieve your brightest smile and are honoured that you're considering us for your dental needs. Please don't hesitate to contact us if you have any questions or to schedule an appointment. We look forward to welcoming you to our practice.</p>
  </div>
  <a class="btn book-online">BOOK ONLINE</a>
</section>

<section class="services">
  <div class="eyebrow">Our Services</div>
  <h2>Comprehensive dental care tailored services for every smile</h2>
  <a class="btn all-services">All Services +</a>

  <div class="card" style="left:160px;width:284px">
    <div class="head"><div class="ic"><svg width="24" height="24" viewBox="0 0 24 24" fill="none" stroke="#fff" stroke-width="1.4"><path d="M7 3c-3 0-4 3-3 6l2 11h2l2-6h4l2 6h2l2-11c1-3 0-6-3-6-2 0-3 1-5 1S9 3 7 3z"/></svg></div>General Dentistry</div>
    <p>Lorem Ipsum is simply dummy text printing when an unknown printer took a galley type and scrambled it to make a type specimen book. It has survived not only recently with</p>
    <div class="pic" role="img" aria-label="Patient smiling in the dental chair" style="background:linear-gradient(135deg,#d8e0e2,#7a5240 55%,#e4e6e3)"></div>
  </div>
  <div class="card" style="left:460px;width:282px">
    <div class="head"><div class="ic"><svg width="24" height="24" viewBox="0 0 24 24" fill="none" stroke="#fff" stroke-width="1.4"><circle cx="12" cy="12" r="8"/><path d="M9 14c1.5 1.5 4.5 1.5 6 0"/></svg></div>Cosmetic Dentistry</div>
    <p>Lorem Ipsum is simply dummy text printing when an unknown printer took a galley type and scrambled it to make a type specimen book. It has survived not only recently with</p>
    <div class="pic" role="img" aria-label="Senior patient with dentist" style="background:linear-gradient(135deg,#d2cdc8,#9a7664 50%,#6f90ad)"></div>
  </div>
  <div class="card" style="left:759px;width:283px">
    <div class="head"><div class="ic"><svg width="24" height="24" viewBox="0 0 24 24" fill="none" stroke="#fff" stroke-width="1.4"><path d="M4 8h16M4 12h16M8 8v4M12 8v4M16 8v4M6 12l1 7h10l1-7"/></svg></div>Teeth Straightening</div>
    <p>Lorem Ipsum is simply dummy text printing when an unknown printer took a galley type and scrambled it to make a type specimen book. It has survived not only recently with</p>
    <div class="pic" role="img" aria-label="Woman holding a clear aligner" style="background:linear-gradient(135deg,#a3b9c1,#c99a80 50%,#b1c5cb)"></div>
  </div>
</section>

<section class="team">
  <h2>OUR TEAM</h2>
  <div class="intro">
    <p>We are delighted to introduce you to our experienced and compassionate dental team. Our team comprises highly skilled dental professionals who are dedicated to providing you with high-quality dental care services. Led by our experienced dentist, each member of our team brings their own unique set of skills and expertise.</p>
    <p>From our friendly reception staff to our knowledgeable hygienists and assistants, our team is here to ensure that you receive personalised dental care that meets your unique needs and preferences. We take great pride in providing a safe, comfortable, and welcoming environment for our patients, and we look forward to serving you with the utmost care and attention.</p>
  </div>
  <div class="member" style="left:191px">
    <div class="face" role="img" aria-label="Portrait of Owen Hartley" style="background:linear-gradient(160deg,#a9b594,#a06f52 50%,#8e8f90)"></div>
    <h5>Owen Hartley</h5><div class="role">Managing Director</div>
    <div class="bio">Lorem Ipsum is simply dummy text printing and typesetting industry lorem Ipsum has been the industry's standard dummy text</div>
    <div class="social"><i aria-label="Social link"></i><i aria-label="Social link"></i><i aria-label="Social link"></i></div>
  </div>
  <div class="member" style="left:470px">
    <div class="face" role="img" aria-label="Portrait of Mira Hartley" style="background:linear-gradient(160deg,#e4e4e2,#8a5c42 50%,#d5d3d0)"></div>
    <h5>Mira Hartley</h5><div class="role">Managing Director</div>
    <div class="bio">Lorem Ipsum is simply dummy text printing and typesetting industry lorem Ipsum has been the industry's standard dummy text</div>
    <div class="social"><i aria-label="Social link"></i><i aria-label="Social link"></i><i aria-label="Social link"></i></div>
  </div>
  <div class="member" style="left:752px">
    <div class="face" role="img" aria-label="Portrait of Alan Pryce" style="background:linear-gradient(160deg,#d9d9d7,#b48a74 50%,#7c6a5c)"></div>
    <h5>Alan Pryce</h5><div class="role">Managing Director</div>
    <div class="bio">Lorem Ipsum is simply dummy text printing and typesetting industry lorem Ipsum has been the industry's standard dummy text</div>
    <div class="social"><i aria-label="Social link"></i><i aria-label="Social link"></i><i aria-label="Social link"></i></div>
  </div>
</section>

<section class="cta">
  <svg class="notch" width="60" height="32" viewBox="0 0 60 32"><path d="M0 0h60L30 32z" fill="#fff"/></svg>
  <h3>Make your dream smile a reality!</h3>
  <p>Call us or book your appointment today</p>
  <a class="btn">BOOK APPOINTMENT</a>
</section>

<section class="join">
  <h2>Join Our Practice</h2>
  <div class="copy">
    <p>We are delighted to introduce you to our experienced and compassionate dental team. Our team comprises highly skilled dental professionals who are dedicated to providing you with high-quality dental care services. Led by our experienced dentist, each member of our team brings their own unique set of skills and expertise.</p>
    <p>Whether you need a routine examination or a more specialised treatment, we have all the resources to provide you with the best dental care possible. Our practice is always up-to-date with the latest techniques and technologies to make sure that our patients receive the best possible results.</p>
    <p>We understand that dental care can be expensive which is why we offer affordable prices to ensure that everyone has access to quality care. If you'd like to learn more about our practice, please don't hesitate to contact us.</p>
  </div>
  <a class="btn join-btn">JOIN NOW</a>
  <div class="join-img" role="img" aria-label="Smiling dentist holding a dental model"></div>
</section>

<section class="contact">
  <h2>GET IN TOUCH</h2>
  <div class="field" style="left:160px;top:126px;width:432px;height:54px">Enter your name</div>
  <div class="field" style="left:611px;top:126px;width:430px;height:54px">Enter your last name</div>
  <div class="field" style="left:160px;top:198px;width:432px;height:54px">Enter your email</div>
  <div class="field" style="left:611px;top:198px;width:430px;height:54px">Enter your phone</div>
  <div class="field" style="left:160px;top:272px;width:881px;height:111px">Enter your comments</div>
  <a class="btn submit">SUBMIT NOW</a>
</section>

<footer class="footer">
  <div class="copy">© 2025 bramblewickdental.example. All Rights Reserved</div>
  <div class="links"><i aria-label="Social link"></i><i aria-label="Social link"></i><i aria-label="Social link"></i></div>
</footer>

</body>
</html>
```